Brisk Refrigeration. Refrigeration and air conditioning specialists.

We need a website to promote our business. We would a modern simple design using the colours from our logo and black. We want it to be fun but proffesional.

Target Market(s)

Commercial

Number of Pages Required

4 page

Requirements
Must have
• Home Page, About Us, Services and Contact Us.
• 24/7 365 days service available.
• Brisk Refrigeration's dedicated team specialises in commercial refrigeration and air conditioning equipment.
• Based in Joondalup, we cover Perth Metro and surrounding areas.
Nice to have
• KNOWLEDGE . EXPERIENCE . PASSION in bold.
• Our experienced and highly trained technicians provide extensive knowledge and exceptional skills for your commercial refrigeration and air conditioning requirements.
• Pictures of commercial refrigeration.
Should not have
• No mention of domestic services.

```html
<!DOCTYPE html>
<html lang="en">
<head>
<meta charset="utf-8">
<title>Brisk Refrigeration</title>
<link href="https://fonts.googleapis.com/css2?family=Poppins:wght@400;500;600;700&family=Raleway:wght@400;500;600&display=swap" rel="stylesheet">
<style>
:root{
  --lime:#9fe662;
  --lime-dark:#86d14a;
  --navy:#1f2637;
  --footer:#252c3d;
  --footer-bottom:#1c2232;
  --grey-band:#eeeeee;
  --text:#4a4a4a;
  --white:#ffffff;
}
*{margin:0;padding:0;box-sizing:border-box}
html,body{width:1200px;height:2491px;overflow:hidden}
body{position:relative;background:var(--white);font-family:"Raleway",sans-serif;color:var(--text)}
.abs{position:absolute}
h1,h2,h3,h4,.nav,.btn,.brand{font-family:"Poppins",sans-serif}

/* hero */
.hero{left:0;top:0;width:1200px;height:541px;overflow:hidden}
.hero-photo{position:absolute;inset:0;background:
  linear-gradient(180deg,rgba(20,32,28,.55),rgba(20,30,30,.7)),
  linear-gradient(100deg,#3d5a2c 0%,#5b7a3a 25%,#7a6a3a 50%,#4d6d34 70%,#8a5a2e 100%)}
.brand{left:136px;top:22px;color:var(--lime);font-weight:700;font-size:26px;line-height:1;letter-spacing:.5px}
.brand small{display:block;font-size:11px;font-weight:700;letter-spacing:.5px;margin-top:3px}
.nav{left:364px;top:40px;display:flex;font-size:12px;font-weight:600;color:var(--white)}
.nav span{position:relative;margin-right:35px}
.nav span.active::after{content:"";position:absolute;left:0;right:0;bottom:-10px;height:2px;background:var(--lime)}
.header-line{left:136px;top:86px;width:930px;height:1px;background:rgba(255,255,255,.2)}
.call{left:890px;top:22px;color:var(--white)}
.call .icon{position:absolute;left:0;top:6px}
.call p{margin-left:44px;font-family:"Poppins",sans-serif}
.call .small{font-size:11px;opacity:.85}
.call .num{font-size:15px;font-weight:600;margin-top:6px;letter-spacing:.5px}
.hero-title{left:0;width:1200px;top:232px;text-align:center;color:var(--lime);font-size:30px;font-weight:700;letter-spacing:1.5px}
.hero-text{left:232px;width:736px;top:294px;text-align:center;color:var(--white);font-size:14.5px;line-height:24px}
.btn-outline{left:508px;top:395px;width:144px;height:38px;border:1px solid var(--lime);background:rgba(0,0,0,.25);color:var(--white);font-size:11px;font-weight:600;display:flex;align-items:center;justify-content:center;letter-spacing:.4px}
.dots{left:552px;top:457px;display:flex;gap:14px}
.dots i{width:6px;height:6px;border-radius:50%;background:rgba(255,255,255,.5)}
.dots i:first-child{background:var(--lime)}

/* quote */
.quote-band{left:0;top:541px;width:1200px;height:357px;background:var(--grey-band)}
.section-title{left:0;width:1200px;text-align:center;color:#222;font-size:18px;font-weight:600;letter-spacing:.5px}
.quote-text{left:345px;width:510px;top:622px;text-align:center;font-size:12px;line-height:24px;color:#555}
.btn-lime{background:var(--lime);color:#1e2430;font-size:11px;font-weight:600;display:flex;align-items:center;justify-content:center;letter-spacing:.4px}
.photo{border:3px solid #fff;box-shadow:0 0 0 1px #ddd}
.feature h3{font-size:13.5px;font-weight:600;color:#222;text-align:center;letter-spacing:.4px}
.feature p{font-size:11.5px;line-height:25px;color:#666;text-align:center;margin-top:14px;padding:0 20px}

/* what we do */
.what{left:0;top:1173px;width:1200px;height:424px;background:linear-gradient(100deg,var(--lime) 0%,#a6ea6c 50%,var(--lime-dark) 100%)}
.what-title{left:136px;top:1222px;font-size:18px;font-weight:600;color:#1c2230}
.what-text{left:136px;top:1263px;width:525px;font-size:11.5px;line-height:24px;color:#2a3020}
.what-text p+p{margin-top:24px}
.btn-dark{left:132px;top:1506px;width:124px;height:41px;background:var(--navy);color:#fff;font-size:11px;font-weight:600;display:flex;align-items:center;justify-content:center}

/* services */
.card h3{font-size:14.5px;font-weight:600;color:#222;margin-top:18px}
.card p{font-size:11.5px;line-height:22px;color:#666;margin-top:8px}

/* footer */
.footer{left:0;top:2102px;width:1200px;height:348px;background:var(--footer)}
.footer-bottom{left:0;top:2450px;width:1200px;height:41px;background:var(--footer-bottom);color:#8a90a0;font-size:10px;display:flex;align-items:center;justify-content:center}
.cta{left:136px;top:2062px;width:930px;height:90px;background:var(--lime);display:flex;align-items:center}
.cta-label{font-family:"Poppins",sans-serif;font-weight:600;font-size:13px;color:#1c2230;line-height:17px;margin-left:20px;letter-spacing:.5px}
.cta-num{font-family:"Poppins",sans-serif;font-weight:600;font-size:30px;color:#1c2230;margin-left:38px;letter-spacing:.5px}
.cta-input{position:absolute;left:513px;top:29px;width:256px;height:33px;background:#fff;border-radius:17px}
.cta-btn{position:absolute;left:782px;top:29px;width:126px;height:33px;background:var(--navy);border-radius:17px;color:#fff;font-family:"Poppins",sans-serif;font-weight:600;font-size:12px;display:flex;align-items:center;justify-content:center}
.fcol h4{color:var(--lime);font-size:12.5px;font-weight:600;letter-spacing:.4px;margin-bottom:22px}
.fcol li{list-style:none;color:#c8ccd6;font-size:11px;line-height:29px;position:relative;padding-left:20px}
.fcol li::before{content:"›";position:absolute;left:0;color:#6d7486}
.office li{padding-left:32px;line-height:20px;margin-bottom:16px}
.office li::before{content:none}
.office svg{position:absolute;left:0;top:3px}
.social{display:flex;gap:8px}
.social i{width:22px;height:22px;background:#5a6274;display:block}
</style>
</head>
<body>

<section class="hero abs">
  <div class="hero-photo" role="img" aria-label="Supermarket produce aisle with refrigerated display shelves of fresh fruit and vegetables"></div>
</section>
<div class="brand abs">Brisk<small>Refrigeration</small></div>
<nav class="nav abs"><span class="active">HOME</span><span>ABOUT US</span><span>SERVICES</span><span>PRODUCTS</span><span>CONTACT US</span></nav>
<div class="call abs">
  <svg class="icon" width="32" height="32" viewBox="0 0 32 32"><path d="M8 5c1.5-1 3 0 3.8 1.5l2 3.5c.6 1.2.2 2.4-.8 3.2l-1.6 1.2c1.2 2.8 3.4 5 6.2 6.2l1.2-1.6c.8-1 2-1.4 3.2-.8l3.5 2c1.5.8 2.5 2.3 1.5 3.8-1.3 2-3.5 3.5-6 3-7.5-1.7-13.3-7.5-15-15C5.5 8.5 6 6.3 8 5z" fill="#9fe662"/><circle cx="24" cy="8" r="6" fill="#9fe662"/><circle cx="21.5" cy="8" r="1" fill="#1f2637"/><circle cx="24" cy="8" r="1" fill="#1f2637"/><circle cx="26.5" cy="8" r="1" fill="#1f2637"/></svg>
  <p class="small">Call Now Fast Service</p>
  <p class="num">+61 8 5550 0142</p>
</div>
<div class="header-line abs"></div>
<h1 class="hero-title abs">KNOWLEDGE . EXPERIENCE . PASSION</h1>
<p class="hero-text abs">We make it a priority to offer flexible services to &nbsp;accommodate your needs Contact us for pricing,<br>offers and product information. Call or fill out the convenient form and a knowledgeable rep will<br>answer your questions.</p>
<div class="btn-outline btn abs">VIEW SERVICES</div>
<div class="dots abs"><i></i><i></i><i></i></div>

<section class="quote-band abs"></section>
<h2 class="section-title abs" style="top:580px">GET YOUR QUOTE</h2>
<p class="quote-text abs">Contact us for pricing, offers and product information. Call or fill out the convenient form and a<br>knowledgeable rep will answer your questions.</p>
<div class="btn-lime btn abs" style="left:512px;top:692px;width:159px;height:38px">FILL OUT FORM</div>

<div class="photo abs" style="left:136px;top:773px;width:434px;height:238px;background:linear-gradient(180deg,#dfe4ea 0%,#c9d0d8 40%,#7d8790 70%,#b8bec4 100%)" role="img" aria-label="Rooftop rows of commercial air conditioning condenser units"></div>
<div class="photo abs" style="left:634px;top:773px;width:434px;height:238px;background:linear-gradient(90deg,#c9c2b0 0%,#e6dcc8 35%,#b54a3e 60%,#d8cfc0 80%,#a8a298 100%)" role="img" aria-label="Supermarket aisle lined with glass-door refrigerated display cases"></div>
<div class="feature abs" style="left:136px;top:1033px;width:434px"><h3>COMMERCIAL AIR CONDITIONING</h3><p>When it gets hot, we stay cool. Manage energy and operational costs by ensuring your air conditioning system is efficient and working to the highest level of performance.</p></div>
<div class="feature abs" style="left:634px;top:1033px;width:434px"><h3>COMMERCIAL REFRIGERATION</h3><p>Keep things at the perfect temperature in your store's walk-in freezers and reach-in coolers. We help you design and install, upgrade and improve, and operate and maintain your essential equipment.</p></div>

<section class="what abs"></section>
<h2 class="what-title abs">WHAT WE DO</h2>
<div class="what-text abs">
  <p>Brisk Refrigeration is a second-generation family-owned business that specializes in commercial air conditioning and refrigeration. We believe education and experience are what sets us apart from our competitors and train our employees not only through traditional educational sources but with hands-on experience in the field as well.</p>
  <p>Based in Joondalup, BRISK Refrigeration covers Perth Metro and surrounding areas and is able to meet all of your preventative maintenance and emergency service needs. Life doesn't hold to business hours and neither do we. Being available 24/7, 365 days allows you as little down time as possible so you can focus on running your business.</p>
</div>
<div class="btn-dark btn abs">READ MORE</div>
<div class="photo abs" style="left:706px;top:1235px;width:359px;height:274px;background:linear-gradient(120deg,#7f8a96 0%,#b9c2cc 35%,#2f4a7a 65%,#6f7a88 100%)" role="img" aria-label="Technician in a hard hat servicing a refrigeration control panel"></div>

<h2 class="section-title abs" style="top:1643px">OUR SERVICES</h2>
<div class="card abs" style="left:132px;top:1714px;width:287px">
  <div class="photo" style="height:163px;background:linear-gradient(180deg,#a9b3bc 0%,#c8b89a 45%,#8a8f94 70%,#cfd5da 100%)" role="img" aria-label="Crew installing a rooftop HVAC unit"></div>
  <h3>HVAC Installation and Fabrication</h3>
  <p>BRISK Refrigeration is one of the leading commercial air conditioning installation companies in Joondalup .</p>
</div>
<div class="card abs" style="left:458px;top:1714px;width:287px">
  <div class="photo" style="height:163px;background:linear-gradient(90deg,#d6d2c8 0%,#7fa04a 30%,#d9a23a 55%,#c64a3a 75%,#e0dcd2 100%)" role="img" aria-label="Refrigerated grocery shelves stocked with packaged goods"></div>
  <h3>Commercial Refrigeration</h3>
  <p>We help convenience stores, grocery stores, and restaurants in Joondalup and across Perth Metro .</p>
</div>
<div class="card abs" style="left:781px;top:1714px;width:287px">
  <div class="photo" style="height:163px;background:linear-gradient(100deg,#aeb6be 0%,#8e969e 40%,#d8dce0 65%,#4c5560 100%)" role="img" aria-label="Technician checking gauges on an outdoor condenser unit"></div>
  <h3>Service &amp; Maintenance</h3>
  <p>Since the beginning, BRISK Refrigeration has prided itself on customer service, with trained technicians across Perth Metro.</p>
</div>

<footer class="footer abs"></footer>
<div class="cta abs">
  <svg style="margin-left:24px" width="30" height="30" viewBox="0 0 32 32"><path d="M8 4c1.5-1 3 0 3.8 1.5l2 3.5c.6 1.2.2 2.4-.8 3.2l-1.6 1.2c1.2 2.8 3.4 5 6.2 6.2l1.2-1.6c.8-1 2-1.4 3.2-.8l3.5 2c1.5.8 2.5 2.3 1.5 3.8-1.3 2-3.5 3.5-6 3-7.5-1.7-13.3-7.5-15-15C4.5 7.5 6 5.3 8 4z" fill="#1f2637"/></svg>
  <div class="cta-label">MAKE AN QUOTE<br>CALL US :</div>
  <div class="cta-num">+0123 555 019</div>
  <div class="cta-input"><svg style="position:absolute;left:12px;top:12px" width="12" height="9" viewBox="0 0 12 9"><rect width="12" height="9" fill="#b9bec8"/><path d="M0 0l6 5 6-5" stroke="#fff" fill="none"/></svg></div>
  <div class="cta-btn">Subscribe</div>
</div>

<div class="fcol abs" style="left:139px;top:2208px"><h4>Navigation</h4><ul><li>About us</li><li>Services</li><li>Equipment Manufactures</li><li>FAQ's</li><li>Our Clients</li></ul></div>
<div class="fcol abs" style="left:367px;top:2208px"><h4>General Info</h4><ul><li>Home</li><li>Privacy Policy</li><li>Terms &amp; Conditions</li></ul></div>
<div class="fcol office abs" style="left:580px;top:2208px"><h4>Office Info</h4><ul>
  <li><svg width="13" height="13" viewBox="0 0 13 13"><path d="M12 1L1 6l5 1 1 5z" fill="#9fe662"/></svg>27 Harbourview Lane<br>Joondalup WA 6027</li>
  <li><svg width="13" height="13" viewBox="0 0 32 32"><path d="M8 4c1.5-1 3 0 3.8 1.5l2 3.5c.6 1.2.2 2.4-.8 3.2l-1.6 1.2c1.2 2.8 3.4 5 6.2 6.2l1.2-1.6c.8-1 2-1.4 3.2-.8l3.5 2c1.5.8 2.5 2.3 1.5 3.8-1.3 2-3.5 3.5-6 3-7.5-1.7-13.3-7.5-15-15C4.5 7.5 6 5.3 8 4z" fill="#9fe662"/></svg>( 08 ) 5550 0164</li>
  <li><svg width="13" height="10" viewBox="0 0 12 9"><rect width="12" height="9" fill="#9fe662"/><path d="M0 0l6 5 6-5" stroke="#252c3d" fill="none"/></svg>sales@briskrefrigeration.com</li>
</ul></div>
<div class="fcol abs" style="left:814px;top:2208px"><h4>Social Links</h4><div class="social"><i></i><i></i><i></i><i></i><i></i><i></i></div></div>

<div class="footer-bottom abs">© 2014 Brisk Refrigeration.com. All Rights Reserved.</div>
</body>
</html>
```